GHalvor Busisness Card

I am an aerospace consultant and at this time only need business cards.

Industry/Entity Type

Business

Contact Information for Business Card

Halvorsen Associates,LLC
Marcus D. Halvorsen

348 Birch Meadow Drive
Hartwell AL 35612

256-555-0187 (cell)
256-555-0142 (fax)

marcushalvorsen@mailbrook.test

```html
<!DOCTYPE html>
<html lang="en">
<head>
<meta charset="utf-8">
<title>Halvorsen Associates, LLC — Business Card</title>
<link rel="stylesheet" href="https://fonts.googleapis.com/css2?family=PT+Sans+Narrow:wght@700&family=Open+Sans:wght@400;700&display=swap">
<style>
  :root {
    --backdrop: #d9dadc;
    --card-white: #ffffff;
    --ink: #000000;
    --accent-blue: #1a78c2;
    --text-light: #ffffff;
  }
  html, body {
    margin: 0;
    padding: 0;
    width: 1200px;
    height: 1200px;
    overflow: hidden;
    background: var(--backdrop);
  }
  .business-card {
    position: absolute;
    left: 150px;
    top: 344px;
    width: 901px;
    height: 512px;
    background: var(--card-white);
    overflow: hidden;
  }
  .company-name {
    position: absolute;
    left: 56px;
    top: 66px;
    margin: 0;
    font-family: "PT Sans Narrow", "Arial Narrow", sans-serif;
    font-weight: 700;
    font-size: 76px;
    line-height: 1;
    color: var(--ink);
    letter-spacing: 0.5px;
  }
  .rule-accent {
    position: absolute;
    left: 0;
    top: 216px;
    width: 666px;
    height: 8px;
    background: var(--accent-blue);
  }
  .rule-dark {
    position: absolute;
    left: 0;
    top: 230px;
    width: 100%;
    height: 10px;
    background: var(--ink);
  }
  .contact-band {
    position: absolute;
    left: 0;
    top: 248px;
    width: 100%;
    height: 264px;
    background: var(--ink);
    font-family: "Open Sans", Verdana, sans-serif;
    color: var(--text-light);
  }
  .person {
    position: absolute;
    left: 113px;
    top: 51px;
  }
  .person-name {
    margin: 0;
    font-size: 26px;
    font-weight: 700;
    line-height: 34px;
    letter-spacing: 0.5px;
  }
  .person-title {
    margin: 0;
    font-size: 21px;
    font-weight: 400;
    line-height: 30px;
    color: var(--accent-blue);
  }
  .contact-list {
    position: absolute;
    left: 480px;
    top: 64px;
    margin: 0;
    padding: 0;
    list-style: none;
    font-size: 22px;
    line-height: 32px;
  }
  .contact-item {
    position: relative;
    padding-left: 35px;
    margin-bottom: 2px;
    white-space: nowrap;
  }
  .contact-item svg {
    position: absolute;
    left: 0;
    top: 5px;
    width: 22px;
    height: 22px;
  }
</style>
</head>
<body>
  <main class="business-card">
    <h1 class="company-name">Halvorsen Associates,LLC</h1>
    <div class="rule-accent"></div>
    <div class="rule-dark"></div>

    <section class="contact-band">
      <div class="person">
        <p class="person-name">Marcus D. Halvorsen</p>
        <p class="person-title">Aerospace consultant</p>
      </div>

      <ul class="contact-list">
        <li class="contact-item">
          <svg viewBox="0 0 22 22" aria-hidden="true">
            <circle cx="11" cy="11" r="11" fill="#ffffff"/>
            <path d="M4.5 11.5 L11 5.5 L17.5 11.5 H15.5 V16.5 H12.5 V13 H9.5 V16.5 H6.5 V11.5 Z" fill="#1a78c2"/>
          </svg>
          348 Birch Meadow Drive Hartwell<br>AL 35612
        </li>
        <li class="contact-item">
          <svg viewBox="0 0 22 22" aria-hidden="true">
            <circle cx="11" cy="11" r="11" fill="#ffffff"/>
            <path d="M7 5 L9.5 5.5 L10 8.5 L8.5 9.5 Q9.8 12.5 12.5 13.5 L13.5 12 L16.5 12.5 L17 15 Q15 17.5 12 16 Q7 13.5 5.5 8.5 Q5.5 6 7 5 Z" fill="#1a78c2"/>
          </svg>
          256-555-0187
        </li>
        <li class="contact-item">
          <svg viewBox="0 0 22 22" aria-hidden="true">
            <circle cx="11" cy="11" r="11" fill="#ffffff"/>
            <rect x="7.5" y="4.5" width="7" height="5" fill="#1a78c2"/>
            <rect x="5" y="9.5" width="12" height="6.5" rx="1" fill="#1a78c2"/>
            <rect x="8" y="12" width="6" height="1.5" fill="#ffffff"/>
          </svg>
          256-555-0142
        </li>
        <li class="contact-item">
          <svg viewBox="0 0 22 22" aria-hidden="true">
            <circle cx="11" cy="11" r="11" fill="#ffffff"/>
            <rect x="5" y="7" width="12" height="8.5" fill="#1a78c2"/>
            <path d="M5 7 L11 12 L17 7" fill="none" stroke="#ffffff" stroke-width="1.3"/>
          </svg>
          marcushalvorsen@mailbrook.test
        </li>
      </ul>
    </section>
  </main>
</body>
</html>
```